Infographic - Iceberg Strategy Process

We need to develop a simple infographic that shows our process for running a team corporate strategy day. the aim is to simply outline the steps and show that most of the work happens well before a team meets for the company's 'off-site' or strategy day (the work that happens below the waterline). See our website for style reference morrowplk.example

We are team strategy facilitators. We facilitate corporate team strategy days that usually run for 1 or 2 days.

We call our process a collaborative strategy process, because we seeking input and contribution from our clients staff, customers and clients in the weeks ahead of the actual facilitated strategy day.

We believe this is the best way to develop a winning strategy is to talk, engage and generate insight from the people you deliver value to.

Most companies (and teams) think that running a successful team strategy day (or workshop) is about getting their team into a room for the workshop and brainstorming ideas.
It's not. In fact the workshop happens toward the process and there are some key steps that need to happen well before the team ever gets into the room - this is what we are trying to portray in the infographic.

We describe the process as being like an iceberg - meaning that the team strategy day (workshop) is really only the the 'tip of the iceberg' and most of the work is done by talking to leaders, staff and clients well before the teams gets together in a room for the strategy day workshop. The pre-workshop steps are often or never undertaken.

We describe the steps before the workshop as being like that part of an iceberg that's 'below the water' because they're the necessary steps that the workshop attendees never see but they makes up the majority of the work (Only 1/10th of an iceberg is above the water http://en.lorebank.example/wiki/Iceberg - See and read the overview section)

Corin

https://slides.vantory.example/presentation/d/7mTkwqobnuvE3-K9sLfGhPzXaRcYdNwBjmVtlQe2xy4/pub?start=false&loop=false&delayms=60000

Target Market(s)

Businesses and corporate teams in business, finance and professional services

Industry/Entity Type

Call

Font styles to use
Sans Serif

Requirements
Must have
• Morrow PLK Logo
• Morrow PLK website reference
• clean, clear design, alignment with Logo colours (logo .png attached)
• Alignment with design of our website style - clean and corporate. We use Google fonts like Raleway (for headings), Merriweather (for content) in our documents

```html
<!DOCTYPE html>
<html lang="en">
<head>
<meta charset="utf-8">
<title>Collaborative Strategy – The Iceberg Process</title>
<link rel="stylesheet" href="https://fonts.googleapis.com/css2?family=Raleway:wght@500;600;800;900&family=Merriweather:wght@400;700&display=swap">
<style>
  :root {
    --sky: #ffffff;
    --water: #abc5ca;
    --title: #5a8e9a;
    --label-above: #5b8f9b;
    --label-below: #ffffff;
    --ice-light: #7fc1cf;
    --ice-mid: #5f9aa6;
    --ice-dark: #41707a;
    --arrow-above: #1c1c1c;
    --arrow-below: #ffffff;
    --note: #4d7f8a;
    --brand: #3d3632;
  }
  * { margin: 0; padding: 0; box-sizing: border-box; }
  html, body { width: 814px; height: 1200px; overflow: hidden; background: var(--sky); }
  .infographic { position: relative; width: 814px; height: 1200px; overflow: hidden; font-family: "Raleway", sans-serif; }
  .scene { position: absolute; inset: 0; }
  .title {
    position: absolute; top: 2px; left: 0; width: 100%;
    text-align: center; color: var(--title);
    font-family: "Raleway", sans-serif; font-weight: 900;
    font-size: 49px; line-height: 56px; letter-spacing: 0.5px;
  }
  .timeline-label {
    position: absolute; right: 605px; font-size: 15.5px; font-weight: 500;
    white-space: nowrap; transform: translateY(-50%);
  }
  .timeline-label.above { color: var(--label-above); }
  .timeline-label.below { color: var(--label-below); }
  .stage {
    position: absolute; left: 298px; width: 240px; text-align: center;
    color: #eef6f8; font-size: 16.5px; font-weight: 500; line-height: 20px;
    transform: translateY(-50%);
  }
  .stage.highlight { font-size: 26px; font-weight: 800; color: #e6f0f2; }
  .note {
    position: absolute; left: 635px; width: 122px;
    font-family: "Merriweather", serif; font-size: 5.6px; line-height: 6.6px;
    color: var(--note);
  }
  .note.below { color: #ffffff; }
  .note h3 { font-size: 5.6px; font-weight: 700; margin-bottom: 8px; }
  .note p { margin: 0; }
  .brand-name {
    position: absolute; left: 0; width: 100%; top: 1085px;
    text-align: center; color: var(--brand);
    font-family: "Raleway", sans-serif; font-weight: 600;
    font-size: 64px; line-height: 76px; letter-spacing: 1px;
  }
</style>
</head>
<body>
<main class="infographic">
  <svg class="scene" width="814" height="1200" viewBox="0 0 814 1200">
    <defs>
      <linearGradient id="ice-fill" x1="0" y1="0" x2="1" y2="1">
        <stop offset="0" stop-color="#7fc1cf"/>
        <stop offset="0.55" stop-color="#5f9aa6"/>
        <stop offset="1" stop-color="#41707a"/>
      </linearGradient>
    </defs>
    <rect class="water" x="0" y="462" width="814" height="738" fill="var(--water)"/>
    <rect class="iceberg" x="232" y="148" width="352" height="830" rx="14" fill="url(#ice-fill)" role="img" aria-label="Iceberg illustration, small tip above the waterline and a large mass below"/>
    <g class="timeline-arrows" stroke-width="1.4" stroke-dasharray="9 6">
      <line x1="160" y1="285" x2="604" y2="285" stroke="var(--arrow-above)"/>
      <line x1="175" y1="352" x2="604" y2="352" stroke="var(--arrow-above)"/>
      <line x1="175" y1="462" x2="604" y2="462" stroke="var(--arrow-above)"/>
      <line x1="175" y1="561" x2="604" y2="561" stroke="var(--arrow-below)"/>
      <line x1="175" y1="681" x2="604" y2="681" stroke="var(--arrow-below)"/>
    </g>
    <g class="arrowheads">
      <polygon points="603,280 623,285 603,290" fill="var(--arrow-above)"/>
      <polygon points="603,347 623,352 603,357" fill="var(--arrow-above)"/>
      <polygon points="603,457 623,462 603,467" fill="var(--arrow-above)"/>
      <polygon points="603,556 623,561 603,566" fill="var(--arrow-below)"/>
      <polygon points="603,676 623,681 603,686" fill="var(--arrow-below)"/>
    </g>
  </svg>

  <h1 class="title">Collaborative Strategy<br>The Iceberg Process</h1>

  <div class="timeline-label above" style="top:275px">2 Weeks After Workshop</div>
  <div class="timeline-label above" style="top:343px">1 Week After Workshop</div>
  <div class="timeline-label above" style="top:443px">Workshop Week</div>
  <div class="timeline-label below" style="top:552px">1 Week To Go</div>
  <div class="timeline-label below" style="top:672px">2 Weeks To Go</div>
  <div class="timeline-label below" style="top:810px">3 Weeks To Go</div>

  <div class="stage" style="top:268px">Communication<br>and Feedback</div>
  <div class="stage" style="top:329px">Strategy on Page<br>(Strategy Map)</div>
  <div class="stage highlight" style="top:416px">Team Strategy Day</div>
  <div class="stage" style="top:552px">Customer to Staff Insight</div>
  <div class="stage" style="top:672px">Secondary Research</div>
  <div class="stage" style="top:819px">Kickoff<br>and Scoping</div>

  <section class="note" style="top:218px">
    <h3>Seek Feedback &amp; Communication</h3>
    <p>Communicate to the workshop group &amp; seek feedback.<br>Incorporate feedback into strategy document and tweak where needed.<br>Coach the team to be your 'market strategy evangelists' to communicate the strategy throughout the organisation.</p>
  </section>
  <section class="note" style="top:292px">
    <h3>Create Strategy Map &amp; Strategy Summary</h3>
    <p>Create a strategy map on one page<br>Create a Strategy Summary Deck in slide format (10–12 slides)<br>Create an action plan and responsibility pages for pricing, services, target market and promotion strategies</p>
  </section>
  <section class="note" style="top:367px">
    <h3>Team Strategy Workshop</h3>
    <p>Define or review the purpose – 'the reason your company exists'<br>1 Blue Sky – create/define your ideal future<br>2 Objective &amp; Goals – define your goals &amp; objectives<br>3 Positioning – define market positioning vs competitors and alternatives<br>4 Critical Issues – define critical issues for success<br>5 Roadmap – create a 12 month roadmap to meet objectives</p>
  </section>
  <section class="note below" style="top:485px">
    <h3>Generate Insight</h3>
    <p>Generate insight on your company, customer and competitors via:<br>1 customer surveys &amp; conversations<br>2 staff surveys &amp; conversations<br>3 workshop attendee interviews<br>Ask for ideas on "how do you win?", "what should you be doing?" and "if you were running things, what would you do?"</p>
  </section>
  <section class="note below" style="top:591px">
    <h3>Scan the Environment and Hypothesise</h3>
    <p>Internal Scan – review past strategy documents, marketing plans, website.<br>External Scan – assess competitors and alternatives. Look at the impact technology has on decision making.<br>Develop Hypothesis – develop your marketing strategy hypothesis for testing.</p>
  </section>
  <section class="note below" style="top:740px">
    <h3>Define the Purpose of the Workshop.</h3>
    <p>Meet with leaders, senior management and key stakeholders.<br>Define what a successful strategy day will look like.<br>Look for clashes and common ground and create a brief. Finally, make a list of workshop participants.</p>
  </section>

  <p class="brand-name">Morrow PLK</p>
</main>
</body>
</html>
```